Podiatry clinic requires a modern revamp and editing of existing website.

I would like a fresh new look and updated information for my current business website. An easy to navigate site with prominent address and phone number for call to action. We are a podiatry clinic that focuses on general and sports podiatry.
I would like 4 pages; including Home page, About Us, Services & Contact.
www.brambleridgefootcare.com

Target Market(s)

Active working professionals.

Industry/Entity Type

Medical

Coding

Coded - Design and coding required

Number of Pages Required

4 page

Font styles to use
Sans Serif

Colors
6b449b

Requirements
Must have
• A modern look with logo and active images; clean and uncluttered. Visible phone number and address for call to action.
• 4 pages - Home, About Us, Services, Contact.
• Home page - update address & service logos.
• About Us - update of personal information.
• Services - Revamp of existing page.
• Contact page to include Google map, email & phone number.
Nice to have
• Ability to add content easily; eg. a blog or adding video onto Home page.
• Link to Facebook page.

```html
<!DOCTYPE html>
<html lang="en">
<head>
<meta charset="utf-8">
<title>bramble ridge foot care</title>
<link href="https://fonts.googleapis.com/css2?family=Montserrat:wght@300;400;500;600&family=Open+Sans:wght@400;600&family=Great+Vibes&display=swap" rel="stylesheet">
<style>
:root{
  --purple:#6b449b;
  --purple-soft:#9a80c2;
  --purple-deep:#5b3a8a;
  --ink:#2b2b2b;
  --grey:#6a6a6a;
  --line:#cfcfcf;
  --light:#f3f3f3;
  --white:#fff;
}
*{box-sizing:border-box;margin:0;padding:0}
html,body{width:1200px;height:2683px;overflow:hidden}
body{position:relative;font-family:"Open Sans",Arial,sans-serif;color:var(--ink);background:var(--white)}
.abs{position:absolute}

/* header */
.header{left:0;top:0;width:1200px;height:674px;background:var(--purple-soft)}
.hero-photo{left:0;top:0;width:1200px;height:450px}
.hero-title{left:80px;top:188px;font-family:"Great Vibes",cursive;font-size:52px;color:var(--white)}
.hero-sub{left:80px;top:252px;font-family:Montserrat,sans-serif;font-size:29px;color:var(--white)}
.dots{left:1028px;top:440px;display:flex;gap:10px}
.dots span{width:11px;height:11px;border:1.5px solid var(--white);border-radius:50%}
.dots span.on{background:var(--white)}
.brand{left:78px;top:560px;display:flex;align-items:center;gap:12px;font-family:Montserrat,sans-serif;font-weight:600;font-size:26px;color:var(--white)}
.brand i{width:34px;height:34px;border-radius:50%;background:var(--purple);display:block}
.btn-book{left:517px;top:545px;width:250px;height:41px;border-radius:21px;background:var(--white);color:var(--purple);font-family:Montserrat,sans-serif;font-size:15px;display:flex;align-items:center;justify-content:center}
.call{left:790px;top:550px;display:flex;align-items:center;gap:12px;color:var(--white);font-family:Montserrat,sans-serif;font-size:19px}
.call b{font-weight:600}
.nav{top:621px;left:563px;display:flex;gap:0;font-family:Montserrat,sans-serif;font-size:15px;color:var(--white)}
.nav a{color:inherit;text-decoration:none;margin-right:48px}
.nav a:last-child{margin-right:0}

/* welcome */
.welcome{left:0;top:700px;width:1200px;text-align:center}
.welcome h1{margin-top:95px;font-family:Montserrat,sans-serif;font-weight:300;font-size:38px;color:var(--ink)}
.welcome h1 span{color:var(--purple);font-weight:400}
.welcome p{width:920px;margin:22px auto 0;font-size:13.5px;line-height:23px;color:var(--grey)}
.btn-more{display:inline-flex;margin-top:28px;width:146px;height:50px;border-radius:25px;background:var(--purple);color:var(--white);font-family:Montserrat,sans-serif;font-weight:500;font-size:14px;align-items:center;justify-content:center}
.foot-icon{display:block;margin:0 auto}

/* services */
.services{left:0;top:1083px;width:1200px;height:417px}
.services h2{left:0;top:50px;width:1200px;text-align:center;font-family:Montserrat,sans-serif;font-weight:300;font-size:36px;color:var(--ink)}
h2 span,h3 span{color:var(--purple);font-weight:400}
.service-box{left:62px;top:130px;width:1073px;height:199px;background:var(--white)}
.service-card{top:15px;width:250px;height:168px}
.service-card .label{position:absolute;left:0;bottom:0;width:100%;height:48px;background:var(--purple);color:var(--white);font-family:Montserrat,sans-serif;font-size:14.5px;display:flex;align-items:center;justify-content:center}
.service-card.open .label{top:0;bottom:auto}
.service-card .detail{position:absolute;left:0;top:48px;width:100%;height:120px;background:rgba(40,40,40,.75);color:var(--white);font-size:13px;line-height:22px;text-align:center;padding:14px 14px 0}

/* testimonials & blog */
.section-title{font-family:Montserrat,sans-serif;font-weight:300;font-size:36px;color:var(--ink)}
.divider{display:block;margin-top:10px}
.clients{left:80px;top:1550px;width:560px}
.quote{margin-top:30px;font-size:14px;line-height:26px;color:var(--grey)}
.quote q{quotes:none}
.qmark{font-family:Georgia,serif;font-size:40px;color:#aaa;line-height:0;vertical-align:-10px}
.avatar{left:92px;top:1775px;width:114px;height:114px;border-radius:50%;border:4px solid var(--white);box-shadow:0 0 0 2px #ddd;background:linear-gradient(160deg,#e8cf9b,#c99d62)}
.client-name{left:252px;top:1812px;font-family:Montserrat,sans-serif;font-size:18px;color:var(--purple)}
.client-city{left:252px;top:1838px;font-size:12px;font-style:italic;color:#999;letter-spacing:1px}
.blog{left:695px;top:1550px;width:430px}
.post{left:692px;width:440px;height:116px}
.post .thumb{position:absolute;left:0;top:0;width:116px;height:116px;border:3px solid var(--white);box-shadow:0 0 0 1px #ddd}
.post h4{position:absolute;left:130px;top:0;font-family:Montserrat,sans-serif;font-weight:400;font-size:17px;color:var(--ink)}
.post .date{position:absolute;left:130px;top:28px;font-size:11px;color:#999;display:flex;gap:8px;align-items:center}
.post p{position:absolute;left:130px;top:48px;width:300px;font-size:13px;line-height:22px;color:var(--grey)}

/* partners */
.partners{left:0;top:1948px;width:1200px;height:125px;background:var(--light)}
.badge{top:32px;height:60px;border-radius:6px;background:#d9d4e3}

/* contact */
.contact{left:0;top:2073px;width:1200px;height:610px;background:linear-gradient(180deg,#5d5a44 0%,#3e3d30 45%,#2f3029 100%)}
.contact h2{left:0;top:50px;width:1200px;text-align:center;font-family:Montserrat,sans-serif;font-weight:300;font-size:36px;color:var(--white)}
.contact h2 span{color:#b9a3dc}
.field{left:77px;width:438px;height:52px;background:var(--white);border-radius:4px;padding:15px 18px;font-size:13px;color:#999}
.btn-submit{left:77px;top:449px;width:166px;height:50px;border-radius:25px;background:var(--purple);color:var(--white);font-family:Montserrat,sans-serif;font-size:21px;display:flex;align-items:center;justify-content:center}
.map{left:535px;top:155px;width:275px;height:277px;background:#c9c9c7;border:3px solid #e5e5e5}
.address{left:855px;top:155px;width:300px;color:var(--white);font-size:13.5px;line-height:22px}
.address h5{font-family:Montserrat,sans-serif;font-weight:400;font-size:18px;margin-bottom:22px}
.address .row{display:flex;gap:14px;margin-bottom:18px}
.address svg{flex:none}
.footer-band{left:0;top:2540px;width:1200px;height:143px}
.copyright{left:80px;top:2641px;color:var(--white);font-size:12.5px}
.social{left:962px;top:2623px;display:flex;gap:12px}
.social span{width:34px;height:34px;border-radius:50%;background:var(--white)}
</style>
</head>
<body>

<header class="abs header">
  <svg class="abs hero-photo" viewBox="0 0 1200 450" role="img" aria-label="Photo of bare feet walking through shallow water on a beach">
    <defs><linearGradient id="sea" x1="0" y1="0" x2="0" y2="1"><stop offset="0" stop-color="#6e7f86"/><stop offset=".6" stop-color="#8c8a80"/><stop offset="1" stop-color="#b7a898"/></linearGradient></defs>
    <path d="M0 0H1200V440C1140 470 1080 410 1000 400S860 420 760 415 560 390 420 405 200 440 110 420 30 390 0 380Z" fill="url(#sea)"/>
  </svg>
  <div class="abs hero-title">Complete Podiatry Services</div>
  <div class="abs hero-sub">We Treat all FOOT Problems</div>
  <div class="abs dots"><span></span><span></span><span class="on"></span><span></span><span></span></div>

  <div class="abs brand"><i></i>bramble ridge foot care</div>
  <div class="abs btn-book">BOOK AN APPOINTMENT</div>
  <div class="abs call">
    <svg width="26" height="26" viewBox="0 0 24 24"><path d="M6.6 10.8a15 15 0 0 0 6.6 6.6l2.2-2.2c.3-.3.7-.4 1-.2 1.1.4 2.3.6 3.6.6.6 0 1 .4 1 1V20c0 .6-.4 1-1 1A17 17 0 0 1 3 4c0-.6.4-1 1-1h3.5c.6 0 1 .4 1 1 0 1.3.2 2.5.6 3.6.1.3 0 .7-.2 1z" fill="#fff"/></svg>
    <span>CALL US NOW : <b>1300 482 907</b></span>
  </div>
  <nav class="abs nav">
    <a href="#">HOME</a><a href="#">ABOUT US</a><a href="#">PODIATRY SERVICES</a><a href="#">CONTACT</a>
  </nav>
</header>

<section class="abs welcome">
  <svg class="foot-icon" width="24" height="50" viewBox="0 0 24 50" style="position:absolute;left:588px;top:28px"><path d="M9 14c6 0 9 6 7 14-1 5 2 9 1 14-1 5-7 6-9 2-2-5 1-9 0-16-1-6-4-14 1-14z" fill="var(--purple)"/><circle cx="8" cy="6" r="3" fill="var(--purple)"/><circle cx="14" cy="5" r="2" fill="var(--purple)"/><circle cx="18" cy="7" r="1.7" fill="var(--purple)"/></svg>
  <h1>WELCOME TO <span>bramble ridge foot care</span></h1>
  <p>Bramble Ridge Foot Care is a Podiatry clinic in the heart of Melbourne CBD. We are located between Harlow &amp; Penfold Streets in the Harbourline Business Centre / Linden Court Complex. Our podiatrists are fully qualified health professionals who are able to diagnose, treat, manage or help to prevent all medical conditions that affect the feet and lower limb. We provide General Podiatry Treatment and some Specialised Services in relation to various foot conditions, including Sports Injuries, Orthotic Therapy and Nail Surgery.</p>
  <div class="btn-more">KNOW MORE</div>
</section>

<section class="abs services">
  <div class="abs" style="left:0;top:0;width:1200px;height:417px;background:linear-gradient(180deg,#e9e4e1,#d8cbc4 50%,#e7e3e2)" role="img" aria-label="Photo of many bare feet resting on white bedding"></div>
  <h2 class="abs">PODIATRY <span>Services</span></h2>
  <div class="abs service-box">
    <div class="abs service-card open" style="left:15px;background:#6f6a64" role="img" aria-label="Photo of diabetic foot assessment">
      <div class="label">DIABETIC MANAGEMENT</div>
      <div class="detail">Assessment of blood supply/circulation with Doppler Ultrasound; Assessment of nerve sensation via Vibration...</div>
    </div>
    <div class="abs service-card" style="left:281px;background:linear-gradient(160deg,#7d3b7a,#c9b9c6)" role="img" aria-label="Photo of nail surgery treatment"><div class="label">NAIL SURGERY</div></div>
    <div class="abs service-card" style="left:545px;background:linear-gradient(160deg,#e9d8cc,#b9d1df)" role="img" aria-label="Photo of a biomechanical foot assessment"><div class="label">BIOMECHANICAL ASSESSMENT</div></div>
    <div class="abs service-card" style="left:810px;background:linear-gradient(160deg,#dfdde0,#7d9ab7)" role="img" aria-label="Photo of a gait analysis with taped leg"><div class="label">GAIT ANALYSIS</div></div>
  </div>
</section>

<section class="abs clients">
  <h3 class="section-title">WHAT <span>Clients</span> SAY</h3>
  <svg class="divider" width="350" height="24" viewBox="0 0 350 24"><line x1="0" y1="8" x2="350" y2="8" stroke="var(--line)"/><rect x="165" y="0" width="20" height="24" fill="#fff"/><path d="M173 4c3 0 4 3 3 7 0 3 1 5 0 8-1 2-3 2-4 0 0-3 1-5 0-9 0-3-1-6 1-6z" fill="var(--purple)"/></svg>
  <p class="quote"><span class="qmark">&ldquo;</span> Lorem Ipsum is simply dummy text of the printing and typesetting industry. Lorem Ipsum has been the industry's standard dummy text ever since the 1500s, when an unknown printer took a galley of type and scrambled it to make a type specimen book. It has survived not only five centuries. <span class="qmark">&rdquo;</span></p>
</section>
<div class="abs avatar" role="img" aria-label="Portrait photo of the client"></div>
<div class="abs client-name">HAZEL CORRAN</div>
<div class="abs client-city">LONDON</div>

<section class="abs blog">
  <h3 class="section-title">LATEST <span>Blog</span></h3>
  <svg class="divider" width="140" height="24" viewBox="0 0 140 24"><line x1="0" y1="8" x2="140" y2="8" stroke="var(--line)"/><rect x="60" y="0" width="20" height="24" fill="#fff"/><path d="M68 4c3 0 4 3 3 7 0 3 1 5 0 8-1 2-3 2-4 0 0-3 1-5 0-9 0-3-1-6 1-6z" fill="var(--purple)"/></svg>
</section>
<article class="abs post" style="top:1648px">
  <div class="thumb" style="background:linear-gradient(160deg,#c7cfd6,#d9b89a)" role="img" aria-label="Photo of a woman stretching after exercise"></div>
  <h4>Lorem Ipsum is simply dummy</h4>
  <div class="date"><svg width="11" height="11" viewBox="0 0 11 11"><rect x=".5" y="1.5" width="10" height="9" fill="none" stroke="var(--purple)"/><rect x=".5" y="1.5" width="10" height="3" fill="var(--purple)"/></svg>20 March 2016</div>
  <p>Lorem Ipsum is simply dummy text of the printing and typesetting industry. Lorem Ipsum has been the industry's standard</p>
</article>
<article class="abs post" style="top:1783px">
  <div class="thumb" style="background:linear-gradient(160deg,#6f7b5e,#8fae4a)" role="img" aria-label="Photo of a runner tying shoes on grass"></div>
  <h4>Lorem Ipsum is simply dummy</h4>
  <div class="date"><svg width="11" height="11" viewBox="0 0 11 11"><rect x=".5" y="1.5" width="10" height="9" fill="none" stroke="var(--purple)"/><rect x=".5" y="1.5" width="10" height="3" fill="var(--purple)"/></svg>20 March 2016</div>
  <p>Lorem Ipsum is simply dummy text of the printing and typesetting industry. Lorem Ipsum has been the industry's standard</p>
</article>

<section class="abs partners" aria-label="Partner badges">
  <div class="abs badge" style="left:125px;width:160px"></div>
  <div class="abs badge" style="left:392px;width:155px"></div>
  <div class="abs badge" style="left:628px;width:157px"></div>
  <div class="abs badge" style="left:883px;width:230px"></div>
</section>

<section class="abs contact">
  <div class="abs" style="left:760px;top:60px;width:260px;height:540px;background:radial-gradient(ellipse at center,rgba(40,50,80,.55),rgba(0,0,0,0) 70%)" role="img" aria-label="Photo of a man running along a country road"></div>
  <h2 class="abs">CONTACT <span>US</span></h2>
  <svg class="abs" style="left:462px;top:104px" width="276" height="24" viewBox="0 0 276 24"><line x1="0" y1="8" x2="276" y2="8" stroke="#ddd"/><path d="M137 4c3 0 4 3 3 7 0 3 1 5 0 8-1 2-3 2-4 0 0-3 1-5 0-9 0-3-1-6 1-6z" fill="#fff"/></svg>
  <div class="abs field" style="top:155px">Name</div>
  <div class="abs field" style="top:212px">E-Mail</div>
  <div class="abs field" style="top:270px">Phone</div>
  <div class="abs field" style="top:327px;height:105px">Message</div>
  <div class="abs btn-submit">SUBMIT</div>
  <div class="abs map" role="img" aria-label="Street map showing the clinic location"></div>
  <div class="abs address">
    <h5>CONTACT ADDRESS</h5>
    <div class="row"><svg width="22" height="26" viewBox="0 0 22 26"><path d="M11 1a8 8 0 0 1 8 8c0 6-8 15-8 15S3 15 3 9a8 8 0 0 1 8-8z" fill="none" stroke="#fff" stroke-width="1.5"/><circle cx="11" cy="9" r="3" fill="none" stroke="#fff" stroke-width="1.5"/></svg><span>Suite 214 / 360 Harlow Street<br>Melbourne 3000.</span></div>
    <div class="row"><svg width="22" height="20" viewBox="0 0 24 24"><path d="M6.6 10.8a15 15 0 0 0 6.6 6.6l2.2-2.2c.3-.3.7-.4 1-.2 1.1.4 2.3.6 3.6.6.6 0 1 .4 1 1V20c0 .6-.4 1-1 1A17 17 0 0 1 3 4c0-.6.4-1 1-1h3.5c.6 0 1 .4 1 1 0 1.3.2 2.5.6 3.6.1.3 0 .7-.2 1z" fill="none" stroke="#fff" stroke-width="1.5"/></svg><span>1300 482 907</span></div>
    <div class="row"><svg width="22" height="18" viewBox="0 0 22 18"><rect x="1" y="2" width="20" height="14" fill="none" stroke="#fff" stroke-width="1.5"/><path d="M1 2l10 8 10-8" fill="none" stroke="#fff" stroke-width="1.5"/></svg><span>info@brambleridgefootcare.com</span></div>
  </div>
</section>

<footer>
  <svg class="abs footer-band" viewBox="0 0 1200 143" preserveAspectRatio="none"><path d="M0 30C80 80 160 60 260 60S500 70 640 62 860 55 960 48 1130 20 1200 0V143H0Z" fill="var(--purple)"/></svg>
  <div class="abs copyright">© bramble ridge foot care - 2016. All Rights Reserved.</div>
  <div class="abs social" aria-label="Social links"><span></span><span></span><span></span><span></span></div>
</footer>

</body>
</html>
```